" A empresa desenvolve projetos residenciais, corporativos entre outros para público de médio/alto padrão, bem como acompanhamento/gerenciamento de obra e contam com parceiros na execução do projeto... "

```html
<!DOCTYPE html>
<html lang="pt-BR">
<head>
<meta charset="utf-8">
<title>Envelope Saco — Livia Arantes</title>
<link rel="stylesheet" href="https://fonts.googleapis.com/css2?family=Montserrat:wght@300;400;500&display=swap">
<style>
  :root {
    --bg: #e9e9e9;
    --frame: #ffffff;
    --paper: #f6f6f6;
    --ink: #111111;
    --accent: #f5b81c;
    --text-dark: #555555;
    --text-light: #d9d9d9;
  }
  * { margin: 0; padding: 0; box-sizing: border-box; }
  html, body { width: 1200px; height: 1200px; overflow: hidden; }
  body {
    background: var(--frame);
    font-family: "Montserrat", sans-serif;
    position: relative;
  }
  .board {
    position: absolute;
    left: 12px; top: 12px;
    width: 1176px; height: 1176px;
    background: var(--bg);
  }
  .board-label {
    position: absolute;
    left: 24px; top: 74px;
    font-size: 28px;
    font-weight: 400;
    letter-spacing: 0.5px;
    color: #222;
  }
  .envelope {
    position: absolute;
    width: 400px; height: 600px;
    overflow: hidden;
  }
  .envelope-front {
    left: 200px; top: 355px;
    background: var(--paper);
  }
  .envelope-back {
    left: 600px; top: 300px;
    background: var(--ink);
  }
  .flap {
    position: absolute;
    left: 0; top: 0;
    width: 100%; height: 32px;
  }
  .contact {
    position: absolute;
    left: 50px; top: 500px;
    list-style: none;
    font-size: 7.5px;
    line-height: 10.5px;
    color: var(--text-dark);
  }
  .contact li { display: flex; align-items: center; gap: 5px; }
  .contact .dot {
    width: 5px; height: 5px; border-radius: 50%;
    background: var(--accent); flex: none;
  }
  .contact .gap { width: 5px; flex: none; }
  .front-accent {
    position: absolute;
    right: 0; bottom: 20px;
    width: 8px; height: 3px;
    background: var(--accent);
  }
  .brand {
    position: absolute;
    left: 210px; top: 322px;
    width: 170px;
    text-align: center;
  }
  .brand-mark {
    display: block;
    width: 14px; height: 14px;
    margin: 0 auto 8px;
    border-radius: 50%;
    background: var(--accent);
  }
  .brand-name {
    font-size: 20px;
    font-weight: 300;
    color: var(--text-light);
    letter-spacing: 0.5px;
  }
  .brand-tagline {
    margin-top: 4px;
    font-size: 7px;
    font-weight: 400;
    letter-spacing: 1.5px;
    color: var(--accent);
  }
  .website {
    position: absolute;
    left: 195px; top: 440px;
    width: 190px;
    text-align: center;
    font-size: 9px;
    letter-spacing: 3px;
    color: var(--text-light);
    white-space: nowrap;
  }
</style>
</head>
<body>
  <div class="board">
    <p class="board-label">ENVELOPE SACO</p>
  </div>

  <section class="envelope envelope-front" aria-label="Envelope saco, frente">
    <svg class="flap" viewBox="0 0 400 32" preserveAspectRatio="none" aria-hidden="true">
      <polygon points="0,0 400,0 388,32 12,32" fill="var(--accent)"/>
    </svg>
    <ul class="contact">
      <li><span class="dot"></span>(11) 3456-7890 · 98765-4321</li>
      <li><span class="dot"></span>(11) 91234-5678</li>
      <li><span class="dot"></span>contato@liviaarantes.com.br</li>
      <li><span class="dot"></span>Rua das Palmeiras, 120</li>
      <li><span class="gap"></span>Sala 12 · Centro · CEP 01000-000</li>
      <li><span class="gap"></span>Jardim Aurora · São Paulo/SP</li>
    </ul>
    <span class="front-accent"></span>
  </section>

  <section class="envelope envelope-back" aria-label="Envelope saco, verso">
    <div class="brand">
      <span class="brand-mark"></span>
      <p class="brand-name">Livia Arantes</p>
      <p class="brand-tagline">arquitetura e interiores</p>
    </div>
    <p class="website">www.liviaarantes.com.br</p>
  </section>
</body>
</html>
```